Professional website for psychological services

Create a professional, easy to navigate website using soothing coastal images and incorporate company logo in design. Website is for a small private clinic that provides psychological services and must be appealing to professional men and women. A website I really like is www.velmorlodge.example I would love something like similar.

Target Market(s)

Professional men and women seeking psychological services

Industry/Entity Type

Mental Health

Number of Pages Required

5+ page

Requirements
Must have
• The website must incorporate the logo provided. The name of the company/website is Brindle Oak Wellness Aftercare. Colors must compliment the logo, must be coastal and soothing yet very professional. I would like a website like www.velmorlodge.example
• Pages will be:Home, Services, FAQ and Contact Us. The images included of the building and office are for the contact us page. Under the tab Servies: Individual Psychotherapy, Family Therapy, EMDR I will provide specific content for each.
Nice to have
• I want the website to be easy to navigate and the font easy to read. The writing on the logo is very light and I'm open to changing it slightly if it will be better aesthetically.
Should not have
• Please no pictures of any swimsuits, alcoholic beverages, etc. This is a professional psychological clinic.

```html
<!DOCTYPE html>
<html lang="en">
<head>
<meta charset="utf-8">
<title>Brindle Oak Wellness Aftercare</title>
<link rel="stylesheet" href="https://fonts.googleapis.com/css2?family=Lato:wght@400;700;900&family=Open+Sans:wght@400;600&family=Oswald:wght@500;600&family=Raleway:wght@400;700&display=swap">
<style>
:root{
  --teal:#1fbcd8;
  --teal-dark:#16a6c0;
  --sand:#e8d5bf;
  --sand-light:#f2e6d8;
  --peach:#e9c4a2;
  --ink:#1d1d1f;
  --navy:#1a2a3a;
  --grey:#6f6f6f;
  --line:#dcdcdc;
  --black:#000;
  --white:#fff;
}
*{box-sizing:border-box;margin:0;padding:0}
html,body{width:1200px;height:3529px;overflow:hidden;background:var(--white)}
body{font-family:"Open Sans",sans-serif;color:var(--ink)}
.page{position:relative;width:1200px;height:3529px;overflow:hidden}
.abs{position:absolute}

/* header */
.site-header{position:absolute;left:0;top:0;width:1200px;height:207px;background:var(--white)}
.brand{position:absolute;left:118px;top:40px;display:flex;align-items:center;gap:14px}
.brand-dot{width:34px;height:34px;border-radius:50%;background:var(--teal)}
.brand-name{font-family:"Lato",sans-serif;font-weight:400;font-size:46px;color:var(--teal);line-height:1}
.main-nav{position:absolute;left:607px;top:122px;display:flex;align-items:center;gap:20px;font-family:"Lato",sans-serif;font-weight:900;font-size:22px;letter-spacing:.5px;color:var(--ink)}
.main-nav .sep{width:5px;height:5px;border-radius:50%;background:var(--ink)}
.header-rule{position:absolute;left:0;top:205px;width:1200px;height:7px;background:var(--sand-light)}

/* hero */
.hero{position:absolute;left:0;top:212px;width:1200px;height:635px;
  background:linear-gradient(180deg,#8fa3b8 0%,#c9b3a6 30%,#efa56a 55%,#e07d3e 66%,#7a4a35 80%,#3a2a24 100%)}
.hero-title{position:absolute;left:125px;top:418px;font-family:"Raleway",sans-serif;font-weight:400;font-size:54px;color:var(--ink);line-height:1}
.hero-sub{position:absolute;left:125px;top:474px;font-family:"Raleway",sans-serif;font-weight:700;font-size:54px;color:var(--teal);line-height:1}
.hero-tags{position:absolute;left:127px;top:536px;font-family:"Lato",sans-serif;font-weight:900;font-size:18px;color:var(--ink);letter-spacing:.3px}
.btn-appointment{position:absolute;left:127px;top:586px;width:219px;height:35px;background:var(--sand);font-family:"Lato",sans-serif;font-weight:900;font-size:17px;color:var(--ink);display:flex;align-items:center;justify-content:center}

/* welcome */
.welcome-icon{position:absolute;left:122px;top:942px;width:44px;height:44px;border-radius:50%;background:var(--teal)}
.welcome-title{position:absolute;left:186px;top:940px;font-family:"Raleway",sans-serif;font-size:24px;color:var(--peach)}
.welcome-title b{color:var(--teal);font-weight:700}
.welcome-rule{position:absolute;left:122px;top:974px;width:525px;height:1px;background:var(--line)}
.welcome-text{position:absolute;left:122px;top:1010px;width:525px;font-size:13px;line-height:22px;color:var(--grey);text-align:justify;text-indent:24px}
.btn-more{position:absolute;left:122px;top:1202px;width:128px;height:29px;border-radius:15px;background:var(--sand-light);font-family:"Lato",sans-serif;font-size:11px;color:var(--white);font-weight:700;display:flex;align-items:center;padding-left:22px}
.btn-more .arrow{position:absolute;right:4px;top:4px;width:21px;height:21px;border-radius:50%;background:var(--white);border:1px solid var(--peach)}

.appointment{position:absolute;left:720px;top:950px;width:358px;height:264px;background:#f4f4f4;border:1px solid var(--line)}
.appointment-tab{position:absolute;left:753px;top:936px;width:285px;height:48px;background:var(--teal);color:var(--white);font-family:"Raleway",sans-serif;font-size:20px;display:flex;align-items:center;padding-left:18px}
.field{position:absolute;background:#eaeaea;border:1px solid #d2d2d2;font-size:13px;color:var(--grey);padding:7px 12px}
.field i{color:var(--teal);font-style:normal}
.btn-submit{position:absolute;left:835px;top:1165px;width:120px;height:28px;border-radius:14px;background:var(--sand);color:var(--white);font-family:"Lato",sans-serif;font-size:12px;font-weight:700;display:flex;align-items:center;justify-content:center}

/* services */
.services{position:absolute;left:0;top:1306px;width:1200px;height:777px;background:var(--sand)}
.section-title{position:absolute;left:0;width:1200px;text-align:center;font-family:"Oswald",sans-serif;font-weight:500}
.services .section-title{top:60px;font-size:38px;color:var(--white)}
.services-intro{position:absolute;left:270px;top:156px;width:660px;text-align:center;font-size:15px;line-height:22px;color:var(--white)}
.service-card{position:absolute;top:259px;width:287px;height:423px;background:var(--white)}
.service-photo{width:287px;height:219px}
.service-name{margin-top:22px;text-align:center;font-family:"Raleway",sans-serif;font-weight:700;font-size:23px;line-height:28px;color:var(--teal);padding:0 30px}
.service-divider{width:40px;height:1px;background:var(--line);margin:12px auto}
.service-text{text-align:center;font-size:14px;line-height:21px;color:var(--grey);padding:0 34px}
.service-plus{position:absolute;left:127px;top:403px;width:34px;height:34px}

/* faq */
.faq{position:absolute;left:0;top:2083px;width:1200px;height:618px;background:var(--teal)}
.faq .section-title{top:98px;font-size:40px;color:var(--navy)}
.faq-item{position:absolute;width:466px;height:63px;background:var(--white);box-shadow:0 2px 4px rgba(0,0,0,.15);display:flex;align-items:center;padding-left:26px;gap:18px;font-family:"Lato",sans-serif;font-size:16px;color:var(--ink)}
.faq-item svg{flex:none}

/* contact */
.contact{position:absolute;left:0;top:2701px;width:1200px;height:487px;
  background:linear-gradient(180deg,#5f6b58 0%,#75806a 35%,#8a8574 60%,#6d6a62 100%)}
.contact .title{position:absolute;left:654px;top:82px;font-family:"Oswald",sans-serif;font-weight:500;font-size:40px;color:var(--white)}
.cfield{position:absolute;background:var(--white);font-family:"Lato",sans-serif;font-size:14px;color:var(--grey);padding:8px 12px}
.btn-send{position:absolute;left:654px;top:363px;width:132px;height:35px;border-radius:18px;background:var(--sand);font-family:"Lato",sans-serif;font-weight:900;font-size:15px;color:var(--ink);display:flex;align-items:center;justify-content:center}

/* footer */
.site-footer{position:absolute;left:0;top:3188px;width:1200px;height:290px;background:var(--black);color:var(--white);font-family:"Lato",sans-serif}
.footer-brand{position:absolute;left:59px;top:68px;display:flex;align-items:center;gap:10px}
.footer-brand .brand-dot{width:22px;height:22px}
.footer-brand .brand-name{font-size:32px}
.footer-phone{position:absolute;left:71px;top:198px;font-size:22px;font-weight:900;color:var(--teal)}
.footer-rule{position:absolute;top:64px;width:1px;height:183px;background:#555}
.footer-head{position:absolute;top:68px;font-size:18px;font-weight:900;letter-spacing:.5px}
.footer-line{position:absolute;font-size:14px;line-height:19px;color:#ddd}
.footer-link{position:absolute;left:624px;font-size:15px;color:#ddd}
.footer-link::before{content:"›";margin-right:12px;color:var(--white)}
.social{position:absolute;top:205px;width:24px;height:24px;background:#555}
.bottom-bar{position:absolute;left:0;top:3478px;width:1200px;height:51px;background:var(--sand);font-family:"Lato",sans-serif;font-size:11px;color:var(--ink);display:flex;align-items:center;justify-content:center}
</style>
</head>
<body>
<div class="page">

  <header class="site-header">
    <div class="brand"><span class="brand-dot"></span><span class="brand-name">Brindle Oak</span></div>
    <nav class="main-nav">
      <span>HOME</span><span class="sep"></span><span>SERVICES</span><span class="sep"></span><span>FAQ</span><span class="sep"></span><span>CONTACT US</span>
    </nav>
  </header>
  <div class="header-rule"></div>

  <section class="hero" role="img" aria-label="Woman on a beach at sunset holding red balloons above the sea"></section>
  <div class="hero-title">Brindle Oak</div>
  <div class="hero-sub">Wellness Aftercare.</div>
  <div class="hero-tags">INDIVIDUAL PSYCHOTHERAPY &nbsp;|&nbsp; FAMILY THERAPY &nbsp;|&nbsp; EMDR</div>
  <div class="btn-appointment">MAKE APPOINTMENT</div>

  <div class="welcome-icon"></div>
  <h2 class="welcome-title">Welcome to <b>Brindle Oak</b></h2>
  <div class="welcome-rule"></div>
  <p class="welcome-text">Lorem ipsum dolor sit amet, consectetuer adipiscing elit. Aenean commodo ligula eget dolor. Aenean massa. Cum sociis natoque penatibus et magnis dis parturient montes, nascetur ridiculus mus. Donec quam felis, ultricies nec, pellentesque eu, pretium quis, sem. Nulla consequat massa quis enim. Donec pede justo, fringilla vel, aliquet nec, vulputate eget, arcu. In enim justo, rhoncus ut, imperdiet a, venenatis vitae, justo. Nullam dictum felis eu pede mollis pretium. Integer tincidunt. Cras dapibus. Vivamus elementum semper nisi. Aenean vulputate eleifend tellus. Aenean leo ligula, porttitor eu, blandit vel Cras dapibus. Vivamus elementum semper nisi.</p>
  <div class="btn-more">READ MORE<span class="arrow"></span></div>

  <div class="appointment"></div>
  <div class="appointment-tab">Schedule your Appointment</div>
  <div class="field" style="left:748px;top:998px;width:302px;height:33px">Name<i>*</i></div>
  <div class="field" style="left:748px;top:1038px;width:302px;height:33px">Email<i>*</i></div>
  <div class="field" style="left:748px;top:1078px;width:302px;height:75px">Message<i>*</i></div>
  <div class="btn-submit">SUBMIT</div>

  <section class="services">
    <h2 class="section-title">Psychotherapy Services</h2>
    <p class="services-intro">Lorem ipsum dolor sit amet, consectetur adipiscing elit. Quid autem habent admirationis, cum prope accesseris? An hoc usque quaque, aliter in vita?</p>

    <article class="service-card" style="left:141px">
      <div class="service-photo" role="img" aria-label="Therapist in session with an older client in a bright office" style="background:linear-gradient(135deg,#c9b9a4,#8a7b70 60%,#4a5570)"></div>
      <h3 class="service-name">Individual Psychotherapy</h3>
      <div class="service-divider"></div>
      <p class="service-text">Lorem ipsum dolor sit amet, consectetur adipiscing elit. Quid autem habent admirationis.</p>
      <svg class="service-plus" viewBox="0 0 34 34"><circle cx="17" cy="17" r="15" fill="#fff" stroke="#1fbcd8" stroke-width="1.5"/><path d="M17 10v14M10 17h14" stroke="#1fbcd8" stroke-width="1.5"/></svg>
    </article>

    <article class="service-card" style="left:456px">
      <div class="service-photo" role="img" aria-label="Family of parents and children sitting together on a sofa" style="background:linear-gradient(135deg,#d8d0c4,#9a8a80 55%,#6a5a78)"></div>
      <h3 class="service-name">Family Therapy</h3>
      <div class="service-divider"></div>
      <p class="service-text">An hoc usque quaque, aliter in vita? Non igitur de improbo, sed de callido improbo quaerimus, qualis Q. Nam quibus rebus efficiuntur</p>
      <svg class="service-plus" viewBox="0 0 34 34"><circle cx="17" cy="17" r="15" fill="#fff" stroke="#1fbcd8" stroke-width="1.5"/><path d="M17 10v14M10 17h14" stroke="#1fbcd8" stroke-width="1.5"/></svg>
    </article>

    <article class="service-card" style="left:772px">
      <div class="service-photo" role="img" aria-label="Close-up of an eye with a multicoloured iris" style="background:linear-gradient(135deg,#e4e4e4,#9a9a9a 55%,#5a5a5a)"></div>
      <h3 class="service-name">EMDR</h3>
      <div class="service-divider"></div>
      <p class="service-text">Negare non possum. Huic mori optimum esse propter desperationem sapientiae, illi propter spem vivere. Quid enim me prohiberet</p>
      <svg class="service-plus" viewBox="0 0 34 34"><circle cx="17" cy="17" r="15" fill="#fff" stroke="#1fbcd8" stroke-width="1.5"/><path d="M17 10v14M10 17h14" stroke="#1fbcd8" stroke-width="1.5"/></svg>
    </article>
  </section>

  <section class="faq">
    <h2 class="section-title">Frequent Ask Questions</h2>
  </section>
  <div class="faq-item" style="left:122px;top:2297px"><svg width="14" height="14" viewBox="0 0 14 14"><rect x=".5" y=".5" width="13" height="13" fill="none" stroke="#1d1d1f"/><path d="M7 3.5v7M3.5 7h7" stroke="#1d1d1f"/></svg>How do I know when it is time to get support?</div>
  <div class="faq-item" style="left:612px;top:2297px"><svg width="14" height="14" viewBox="0 0 14 14"><rect x=".5" y=".5" width="13" height="13" fill="none" stroke="#1d1d1f"/><path d="M7 3.5v7M3.5 7h7" stroke="#1d1d1f"/></svg>How do I know when it is time to get support?</div>
  <div class="faq-item" style="left:122px;top:2377px"><svg width="14" height="14" viewBox="0 0 14 14"><rect x=".5" y=".5" width="13" height="13" fill="none" stroke="#1d1d1f"/><path d="M7 3.5v7M3.5 7h7" stroke="#1d1d1f"/></svg>What is a Marriage and Family Therapist?</div>
  <div class="faq-item" style="left:612px;top:2377px"><svg width="14" height="14" viewBox="0 0 14 14"><rect x=".5" y=".5" width="13" height="13" fill="none" stroke="#1d1d1f"/><path d="M7 3.5v7M3.5 7h7" stroke="#1d1d1f"/></svg>What is a Marriage and Family Therapist?</div>
  <div class="faq-item" style="left:122px;top:2454px"><svg width="14" height="14" viewBox="0 0 14 14"><rect x=".5" y=".5" width="13" height="13" fill="none" stroke="#1d1d1f"/><path d="M7 3.5v7M3.5 7h7" stroke="#1d1d1f"/></svg>How long does therapy last?</div>
  <div class="faq-item" style="left:612px;top:2454px"><svg width="14" height="14" viewBox="0 0 14 14"><rect x=".5" y=".5" width="13" height="13" fill="none" stroke="#1d1d1f"/><path d="M7 3.5v7M3.5 7h7" stroke="#1d1d1f"/></svg>How long does therapy last?</div>
  <div class="faq-item" style="left:122px;top:2534px"><svg width="14" height="14" viewBox="0 0 14 14"><rect x=".5" y=".5" width="13" height="13" fill="none" stroke="#1d1d1f"/><path d="M7 3.5v7M3.5 7h7" stroke="#1d1d1f"/></svg>What type of therapy is offered?</div>
  <div class="faq-item" style="left:612px;top:2534px"><svg width="14" height="14" viewBox="0 0 14 14"><rect x=".5" y=".5" width="13" height="13" fill="none" stroke="#1d1d1f"/><path d="M7 3.5v7M3.5 7h7" stroke="#1d1d1f"/></svg>What type of therapy is offered?</div>

  <section class="contact" role="img" aria-label="Clinic building behind palm trees, softly darkened">
    <h2 class="title">Contact Us</h2>
    <div class="cfield" style="left:654px;top:167px;width:205px;height:36px">Name</div>
    <div class="cfield" style="left:880px;top:167px;width:202px;height:36px">Email</div>
    <div class="cfield" style="left:654px;top:210px;width:205px;height:35px">Phone</div>
    <div class="cfield" style="left:880px;top:210px;width:202px;height:35px">I want to discuss</div>
    <div class="cfield" style="left:654px;top:257px;width:428px;height:82px">Special Request</div>
    <div class="btn-send">Submit Now</div>
  </section>

  <footer class="site-footer">
    <div class="footer-brand"><span class="brand-dot"></span><span class="brand-name">Brindle Oak</span></div>
    <div class="footer-phone">800-555-0142</div>

    <div class="footer-rule" style="left:282px"></div>
    <div class="footer-rule" style="left:562px"></div>
    <div class="footer-rule" style="left:812px"></div>

    <div class="footer-head" style="left:320px">CONTACT</div>
    <svg class="abs" style="left:320px;top:116px" width="11" height="15" viewBox="0 0 11 15"><path d="M5.5 0A5.5 5.5 0 0 0 0 5.5C0 9.5 5.5 15 5.5 15S11 9.5 11 5.5A5.5 5.5 0 0 0 5.5 0Z" fill="#fff"/><circle cx="5.5" cy="5.5" r="2" fill="#000"/></svg>
    <div class="footer-line" style="left:342px;top:114px">Harlow Point Counseling, P.C.<br>418 Tidewater Lane<br>Marlow Bay, GA 30000</div>
    <svg class="abs" style="left:320px;top:220px" width="12" height="9" viewBox="0 0 12 9"><rect width="12" height="9" fill="#fff"/><path d="M0 0l6 5 6-5" fill="none" stroke="#000"/></svg>
    <div class="footer-line" style="left:342px;top:214px">hello@brindleoak.example</div>

    <div class="footer-head" style="left:624px">COMPANY</div>
    <div class="footer-link" style="top:113px">Home</div>
    <div class="footer-link" style="top:146px">Services</div>
    <div class="footer-link" style="top:177px">Faq</div>
    <div class="footer-link" style="top:208px">Contact us</div>

    <div class="footer-head" style="left:875px">OPEN HOURS</div>
    <div class="footer-line" style="left:875px;top:112px;font-size:15px;line-height:29px">Monday-Friday 3pm-9pm<br>Saturday 8am-4pm<br>Sunday closed</div>
    <div class="social" style="left:875px"></div>
    <div class="social" style="left:907px"></div>
    <div class="social" style="left:939px"></div>
    <div class="social" style="left:971px"></div>
  </footer>
  <div class="bottom-bar">© 2018 brindle oak &nbsp;|&nbsp; All Rights Reserved &nbsp;|&nbsp; Disclaimer &nbsp;|&nbsp; Privacy Policy</div>

</div>
</body>
</html>
```